Wendlemoor Contracting In need of monthly newsletter

We need a monthly newsletter to promote our monthly special of Mulch Installation.

Please change wording to fit what you feel is professional and effective.

Our regular price to install Mulch is $169/Yard installed/Delivered

We would like to run a promotion of $125/Yard Installed & Delivered

Compare us to others $135/Yard Delivered only from some other suppliers

Also list somewhere on the newsletter :
- Delivery of soils, stone, wood also available
- Check out our website
- an emphasis on quality

The Fine Print
* Some Conditions apply
Mulches included in sale Dusk Velvet, Chocolate Brown, Auburn Red, Natural, Hemlock, Gold, Shredded Pine. Some site conditions may incur extra cost. minimum 3 Yards for sale price to be in effect, HST extra on all prices listed,

CHECK OUR WEBSITE FOR SOME IMAGES AND MORE INFORMATION....

ASK ANYTHING YOU WANT VIA Pixel Bazaar

Types of Mulch have changed Slightly in the "Fine Print"

Classic Cedar, Black Cedar, Red Cedar, Chocolate brown, Pine Bark, Natural Shredded Pine, Hemlock, Utility Style.

We will also be submitting pictures of the mulch HOWEVER you might need to crop or alter these images to make them work for our newsletter.

Reason: We have not yet found a design we think is Straight to the point. Simple and with our theme.

```html
<!DOCTYPE html>
<html lang="en">
<head>
<meta charset="utf-8">
<title>Wendlemoor Contracting – Monthly Mulch Special</title>
<link rel="stylesheet" href="https://fonts.googleapis.com/css2?family=Open+Sans:wght@400;600;700&display=swap">
<style>
:root{
  --ink:#2b2b2b;
  --text:#555555;
  --muted:#8a8a8a;
  --panel:#e6e6e6;
  --ring:#e2e2e2;
  --dark:#222222;
  --green:#1d6a1d;
  --button:#2f9a2f;
  --red:#e0443a;
  --white:#ffffff;
  --rule:#dddddd;
  --bracket:#9a9a9a;
}
*{box-sizing:border-box;margin:0;padding:0}
html,body{width:1200px;height:2826px;overflow:hidden;background:var(--white)}
body{position:relative;font-family:"Open Sans",Arial,sans-serif;color:var(--text)}
.abs{position:absolute}

/* header */
.brand{left:166px;top:34px;display:flex;align-items:center;gap:18px}
.brand-mark{width:92px;height:92px;border-radius:50%;border:9px solid var(--ink)}
.brand-name{font-weight:600;color:var(--ink);font-size:27px;line-height:30px;letter-spacing:1px;text-transform:uppercase}
.social{right:166px;top:52px;display:flex;gap:12px;font-size:14px;font-weight:600;color:var(--ink);white-space:nowrap}
.contact{right:166px;top:84px;font-size:18px;font-weight:600;color:var(--ink);white-space:nowrap}

/* hero */
.hero{left:150px;top:165px;width:894px;height:416px;background:var(--panel);overflow:hidden}
.hero-bar{left:0;bottom:0;width:100%;height:62px;background:var(--dark);color:var(--white);font-size:21px;line-height:62px;padding-left:18px;text-transform:uppercase;white-space:nowrap}
.offer{left:36px;top:0;width:360px;height:354px;text-align:center;color:var(--ink)}
.offer-big{left:0;top:42px;width:100%;font-size:76px;font-weight:600;line-height:90px;white-space:nowrap}
.offer-price{left:0;width:100%;font-size:16px;font-weight:700;line-height:24px;text-transform:uppercase;white-space:nowrap}
.offer-new{top:146px}
.offer-old{top:170px;text-decoration:line-through}
.offer-bracket{left:25px;top:202px}
.offer-cta{left:0;top:276px;width:100%;font-size:28px;font-weight:600;line-height:40px;text-transform:uppercase;white-space:nowrap}
.hero-photo{left:470px;top:20px;width:380px;height:380px;z-index:1}

/* photo circles */
.photo{border-radius:50%;border:14px solid var(--ring)}
.photo-lawn{background:radial-gradient(circle at 40% 30%,#7a8f6a 0%,#4e7a33 45%,#6b2f1c 75%,#4a9a2a 100%)}
.photo-stone{background:linear-gradient(180deg,#7d96b4 0%,#a8b6c4 35%,#5a6c7c 55%,#cfc5b5 75%,#8d8174 100%)}
.photo-soil{background:linear-gradient(180deg,#4f79b8 0%,#9fb8d8 45%,#d8cdbf 60%,#b79668 80%,#8c6b45 100%)}
.photo-wood{background:linear-gradient(160deg,#3f4a3a 0%,#6e6a5e 35%,#b98a5b 60%,#8a5a35 85%,#5e3c22 100%)}

/* services */
.service-photo{width:338px;height:338px}
.service-title{font-size:31px;font-weight:600;color:var(--green);margin-bottom:12px}
.service-copy{font-size:17px;line-height:30px}
.service-text{width:500px}

/* call to action */
.cta{left:150px;top:1828px;width:894px;height:71px;background:var(--panel)}
.cta-text{left:16px;top:0;line-height:71px;font-size:26px;color:var(--ink);white-space:nowrap}
.cta-button{right:14px;top:15px;width:144px;height:42px;background:var(--button);color:var(--white);font-size:25px;line-height:42px;text-align:center;border-radius:3px}

/* features */
.feature{width:420px;top:1980px}
.feature-title{font-size:21px;font-weight:700;color:var(--ink);text-transform:uppercase;margin-bottom:10px}
.feature-copy{font-size:17px;line-height:28px}
.feature-link{display:block;margin-top:22px;font-size:17px;color:var(--red)}
.divider{left:592px;top:1940px;width:1px;height:270px;background:var(--rule)}

/* partners */
.partners{left:150px;top:2246px;width:894px;height:132px;background:var(--panel);display:flex;justify-content:space-around;align-items:center}
.badge{background:#b8b8b8}
.badge-a{width:172px;height:66px;border-radius:6px;background:#1f5a7a}
.badge-b{width:176px;height:40px}
.badge-c{width:128px;height:56px;background:#4a5fa8}
.badge-d{width:208px;height:44px;background:#3b4aa0}

/* fine print */
.conditions-title{left:168px;top:2434px;font-size:27px;font-weight:600;color:var(--ink);text-transform:uppercase}
.mulch-list{list-style:none;font-size:18px;line-height:30px;color:var(--text);text-transform:uppercase;white-space:nowrap}
.mulch-list li::before{content:"–";margin-right:18px;color:var(--muted)}
.fine-print{left:150px;top:2630px;width:894px;text-align:center;font-size:18px;line-height:32px}

/* footer */
.footer-rule{left:150px;top:2743px;width:894px;height:1px;background:var(--rule)}
.copyright{left:150px;top:2766px;font-size:16px;color:var(--text)}
.payments{right:156px;top:2766px;display:flex;gap:14px;font-size:14px;font-weight:600;color:var(--ink);white-space:nowrap}
</style>
</head>
<body>

<header>
  <div class="abs brand">
    <span class="brand-mark"></span>
    <div class="brand-name">Wendlemoor<br>Contracting<br>Group</div>
  </div>
  <nav class="abs social">
    <span>Quillpost</span><span>Brindlefeed</span><span>Orbichatter</span><span>Nookshare</span><span>Reelwisp</span>
  </nav>
  <div class="abs contact">info@wendlemoorcontracting.com</div>
</header>

<section class="abs hero">
  <div class="abs offer">
    <div class="abs offer-big">30% OFF</div>
    <div class="abs offer-price offer-new">$125/yard installed &amp; delivered</div>
    <div class="abs offer-price offer-old">$169/yard installed/delivered</div>
    <svg class="abs offer-bracket" width="310" height="60" viewBox="0 0 310 60" aria-hidden="true">
      <path d="M4 0 V20 Q4 30 14 30 H140 L155 54 L170 30 H296 Q306 30 306 20 V0" fill="none" stroke="#9a9a9a" stroke-width="6"/>
    </svg>
    <div class="abs offer-cta">Order now</div>
  </div>
  <div class="abs photo photo-lawn hero-photo" role="img" aria-label="Freshly mulched garden bed with a tree and green lawn"></div>
  <div class="abs hero-bar">Minimum 3 yards for sale price to be in effec</div>
</section>

<section>
  <div class="abs photo photo-stone service-photo" style="left:153px;top:684px" role="img" aria-label="Stacked pale stones by the water"></div>
  <div class="abs service-text" style="left:512px;top:714px">
    <h2 class="service-title">Delivery of Stone</h2>
    <p class="service-copy">Sed ut perspiciatis unde omnis iste natus error sit voluptatem accusantium doloremque laudantium, totam rem aperiam, eaque ipsa quae ab illo inventore veritatis et quasi architecto beatae vitae dicta sunt explicabo. Nemo enim ipsam voluptatem quia voluptas sit aspernatur aut odit aut fugit, sed quia consequuntur magni dolores eos qui ratione voluptatem sequi nesciunt.</p>
  </div>

  <div class="abs service-text" style="left:164px;top:1096px">
    <h2 class="service-title">Delivery of Soils</h2>
    <p class="service-copy">Sed ut perspiciatis unde omnis iste natus error sit voluptatem accusantium doloremque laudantium, totam rem aperiam, eaque ipsa quae ab illo inventore veritatis et quasi architecto beatae vitae dicta sunt explicabo. Nemo enim ipsam voluptatem quia voluptas sit aspernatur aut odit aut fugit, sed quia consequuntur magni dolores eos qui ratione voluptatem sequi nesciunt.</p>
  </div>
  <div class="abs photo photo-soil service-photo" style="left:690px;top:1050px" role="img" aria-label="Dump truck tipping a load of soil under blue sky"></div>

  <div class="abs photo photo-wood service-photo" style="left:153px;top:1425px" role="img" aria-label="Pile of split firewood beside a forest"></div>
  <div class="abs service-text" style="left:515px;top:1456px">
    <h2 class="service-title">Delivery of Woods</h2>
    <p class="service-copy">Sed ut perspiciatis unde omnis iste natus error sit voluptatem accusantium doloremque laudantium, totam rem aperiam, eaque ipsa quae ab illo inventore veritatis et quasi architecto beatae vitae dicta sunt explicabo. Nemo enim ipsam voluptatem quia voluptas sit aspernatur aut odit aut fugit, sed quia consequuntur magni dolores eos qui ratione voluptatem sequi nesciunt.</p>
  </div>
</section>

<section class="abs cta">
  <div class="abs cta-text">Want More Offer Click &amp; Enter The Site</div>
  <div class="abs cta-button">Click Here</div>
</section>

<section>
  <div class="abs feature" style="left:150px">
    <h3 class="feature-title">An emphasis on quality</h3>
    <p class="feature-copy">Lorem ipsum dolor sit amet, consectetur adipisicing elit, sed do eiusmod tempor incididunt ut labore et dolore magna aliqua. Ut enim ad minim veniam, quis nostrud exercitation ullamco laboris nisi ut aliquip ex ea commodo consequat.</p>
    <span class="feature-link">Read More</span>
  </div>
  <div class="abs divider"></div>
  <div class="abs feature" style="left:630px">
    <h3 class="feature-title">Well equiped</h3>
    <p class="feature-copy">Lorem ipsum dolor sit amet, consectetur adipisicing elit, sed do eiusmod tempor incididunt ut labore et dolore magna aliqua. Ut enim ad minim veniam, quis nostrud exercitation ullamco laboris nisi ut aliquip ex ea commodo consequat.</p>
    <span class="feature-link">Read More</span>
  </div>
</section>

<section class="abs partners" aria-label="Partner badges">
  <div class="badge badge-a"></div>
  <div class="badge badge-b"></div>
  <div class="badge badge-c"></div>
  <div class="badge badge-d"></div>
</section>

<section>
  <h2 class="abs conditions-title">Some conditions apply</h2>
  <ul class="abs mulch-list" style="left:168px;top:2512px">
    <li>Classic cedar</li><li>Black cedar</li><li>Red cedar</li>
  </ul>
  <ul class="abs mulch-list" style="left:472px;top:2512px">
    <li>Pine bark</li><li>Natural shredded pine</li><li>Hemlock</li>
  </ul>
  <ul class="abs mulch-list" style="left:816px;top:2516px">
    <li>Chocolate brown</li>
  </ul>
  <p class="abs fine-print">Some site conditions may incur extra cost. minimum 3 Yards for sale price to be in effect, HST extra<br>on all prices listed,</p>
</section>

<footer>
  <div class="abs footer-rule"></div>
  <div class="abs copyright">Copy right 2014 all right reserved</div>
  <div class="abs payments"><span>Tallvane Pay</span><span>Corvexa Card</span></div>
</footer>

</body>
</html>
```